Pop up exhibition stand 2000mm (H) x 800mm (W)

I would like a simple pop up banner stand for an exhibition.

We need a pop up banner stand design for 'Brindle Forge Services'

the size is 2000mm(H) x 800mm (W)

Ad copy as follows :

[Brindle Forge logo]

From Sheet Metal To Large Sand Castings

Our Capacity and Rapid Quenching drop bottom ovens deliver precise processing.
We also serve the leading names in aerospace, automotive and advanced engineering.

Visit www.brindleforge-example.co.uk/ or call us Tel: +44 (0)1632 960318

[Put the crafted across the shires logo here, also include the text member somewhere close]

check on their website for other ideas that can help you with this project.

Target Market(s)

will be used at a trade show

Requirements
Nice to have
• modern design for UK manufacturing business

```html
<!DOCTYPE html>
<html lang="en">
<head>
<meta charset="utf-8">
<title>Brindle Forge Services – Exhibition Banner</title>
<link rel="stylesheet" href="https://fonts.googleapis.com/css2?family=Source+Sans+3:wght@400;600;700&display=swap">
<style>
  :root {
    --red: #d7282f;
    --red-deep: #9e1218;
    --red-soft: #e0464b;
    --ink: #3a3a3a;
    --grey: #8a8a8a;
    --grey-light: #d9d9d9;
    --white: #ffffff;
  }
  * { box-sizing: border-box; margin: 0; padding: 0; }
  html, body { width: 1200px; height: 2536px; overflow: hidden; background: var(--white); }
  body { font-family: "Source Sans 3", "Helvetica Neue", Arial, sans-serif; color: var(--ink); }

  .banner { position: relative; width: 1200px; height: 2536px; background: var(--white); }

  .brand { position: absolute; left: 150px; top: 110px; }
  .brand-name { display: flex; align-items: center; gap: 22px; font-size: 96px; font-weight: 700; color: var(--red); line-height: 1; letter-spacing: -1px; }
  .brand-mark { width: 34px; height: 34px; border-radius: 50%; background: var(--grey-light); }
  .brand-tagline { margin-top: 18px; margin-left: 56px; font-size: 36px; color: var(--grey); line-height: 1.15; }
  .brand-tagline em { display: block; color: var(--red); font-style: italic; }

  .headline { position: absolute; top: 440px; left: 0; width: 100%; text-align: center; font-size: 92px; font-weight: 600; line-height: 1.12; color: var(--red); letter-spacing: -0.5px; }

  .sectors { position: absolute; top: 730px; left: 0; width: 1200px; height: 1100px; display: grid; grid-template-columns: 1fr 1fr; grid-template-rows: repeat(3, 1fr); gap: 6px; }
  .sector { position: relative; overflow: hidden; }
  .sector-photo-neutral { background: linear-gradient(135deg, #c9ccd0 0%, #8e949a 55%, #5b6066 100%); }
  .sector-photo-red { background: linear-gradient(135deg, var(--red-soft) 0%, var(--red) 45%, var(--red-deep) 100%); }
  .sector-label { position: absolute; left: 40px; top: 34px; font-size: 56px; font-weight: 400; color: var(--white); letter-spacing: 1px; text-transform: uppercase; }
  .sector-label-right { left: auto; right: 40px; }

  .intro { position: absolute; top: 1880px; left: 80px; right: 80px; text-align: center; font-size: 42px; line-height: 1.3; color: var(--ink); }
  .intro p + p { margin-top: 34px; }
  .intro strong { font-weight: 700; }

  .membership { position: absolute; top: 2150px; left: 0; width: 100%; display: flex; justify-content: center; align-items: center; gap: 22px; font-size: 24px; color: var(--grey); letter-spacing: 1px; }
  .membership-badge { width: 56px; height: 56px; border-radius: 50%; background: var(--red); }

  .contact { position: absolute; left: 0; bottom: 0; width: 100%; height: 270px; background: var(--red); color: var(--white); text-align: center; padding-top: 58px; }
  .contact-web { font-size: 68px; font-weight: 600; line-height: 1; }
  .contact-phone { margin-top: 24px; font-size: 44px; }
</style>
</head>
<body>
<main class="banner">
  <header class="brand">
    <div class="brand-name"><span class="brand-mark"></span>Brindle Forge</div>
    <p class="brand-tagline">the solution in<em>aluminium heat treatment</em></p>
  </header>

  <h1 class="headline">From Sheet Metal To<br>Large Sand Castings</h1>

  <section class="sectors">
    <div class="sector sector-photo-neutral" role="img" aria-label="Engineer in shirt and tie standing in the workshop"></div>
    <div class="sector sector-photo-red" role="img" aria-label="Red-tinted photo of a car in motion">
      <span class="sector-label sector-label-right">Automotive</span>
    </div>
    <div class="sector sector-photo-red" role="img" aria-label="Red-tinted photo of a passenger jet in flight">
      <span class="sector-label">Aerospace</span>
    </div>
    <div class="sector sector-photo-neutral" role="img" aria-label="Technician inspecting metal parts in the plant"></div>
    <div class="sector sector-photo-neutral" role="img" aria-label="Large metal ring being lifted beside a drop bottom oven"></div>
    <div class="sector sector-photo-red" role="img" aria-label="Red-tinted photo of heat treatment oven racks">
      <span class="sector-label sector-label-right">Engineering</span>
    </div>
  </section>

  <section class="intro">
    <p>Our <strong>Capacity</strong> and <strong>Rapid Quenching</strong> drop bottom ovens deliver <strong>precise</strong> processing.</p>
    <p>We also serve the <strong>leading</strong> names in aerospace, automotive and advanced engineering.</p>
  </section>

  <div class="membership">
    <span>MEMBER OF</span>
    <span class="membership-badge" role="img" aria-label="crafted across the shires membership badge"></span>
  </div>

  <footer class="contact">
    <p class="contact-web">www.brindleforge-example.co.uk</p>
    <p class="contact-phone">call us: +44 (0)1632 960318</p>
  </footer>
</main>
</body>
</html>
```